Tin-lantern-walk.com

The existing website http://www.tin-lantern-walk.com needs to get into shape. I'd like to have it transformed into wordpress with a brand-new design. The design should include a logo for multiple uses.

```html
<!DOCTYPE html>
<html lang="en">
<head>
<meta charset="utf-8">
<title>Tin Lantern Walk</title>
<link href="https://fonts.googleapis.com/css2?family=Open+Sans:wght@400;600&family=Roboto:wght@300;400;500&family=Roboto+Condensed:wght@700&display=swap" rel="stylesheet">
<style>
:root{
  --blue:#0d5bb5;
  --blue-dark:#0a4a98;
  --blue-footer:#0a7fd0;
  --green:#5cb860;
  --text:#555;
  --heading:#444;
  --white:#fff;
  --line:#e3e3e3;
}
*{margin:0;padding:0;box-sizing:border-box}
html,body{width:668px;height:1200px;overflow:hidden;background:#fff}
body{position:relative;font-family:"Open Sans",sans-serif;color:var(--text)}
h1,h2,h3{font-weight:400}
.abs{position:absolute}

/* header */
.site-header{position:absolute;left:0;top:0;width:668px;height:69px;background:#fff}
.brand{left:54px;top:22px;display:flex;align-items:center;gap:7px}
.brand-mark{width:26px;height:26px;border-radius:50%;background:var(--green)}
.brand-name{font-family:"Roboto",sans-serif;font-weight:500;font-size:18px;color:var(--blue);line-height:1;letter-spacing:.2px}
.brand-tag{font-family:"Roboto",sans-serif;font-weight:400;font-size:10px;letter-spacing:1.5px;color:#444;margin-top:2px}
.contact-icon{left:342px;top:25px;width:20px;height:20px;border:1px solid #888;border-radius:50%;display:flex;align-items:center;justify-content:center}
.contact-lines{left:373px;top:23px;font-size:8px;line-height:13px;color:#555}
.search{left:483px;top:26px;width:130px;height:20px;border:1px solid var(--line);font-size:6.5px;color:#333;padding:6px 7px;display:flex;justify-content:space-between;align-items:center}

/* nav */
.main-nav{left:0;top:69px;width:668px;height:29px;background:var(--blue);border-bottom:1px solid var(--blue-dark)}
.nav-item{position:absolute;top:0;height:29px;line-height:29px;font-family:"Roboto",sans-serif;font-size:7.5px;color:var(--white)}
.nav-home{left:54px;width:59px;background:var(--green);text-align:center}
.nav-sep{position:absolute;top:0;width:1px;height:29px;background:rgba(255,255,255,.12)}

/* hero */
.hero{left:0;top:98px;width:668px;height:287px;background:linear-gradient(100deg,#1d2f66 0%,#3a4f7e 22%,#d5d8de 42%,#c9ccd2 70%,#3a56a0 100%)}
.hero-title{left:54px;top:191px;font-family:"Roboto Condensed",sans-serif;font-weight:700;font-size:23px;color:var(--white);letter-spacing:.2px}
.hero-text{left:55px;top:222px;width:210px;font-size:7px;line-height:12px;color:var(--white)}
.hero-btn{left:54px;top:258px;width:83px;height:21px;background:var(--green);border:1px solid #7ccf7f;border-radius:2px;color:var(--white);font-family:"Roboto",sans-serif;font-size:8.5px;text-align:center;line-height:19px}
.dots{left:55px;top:295px;display:flex;gap:3px}
.dot{width:10px;height:10px;border-radius:50%;border:1.2px solid #fff}
.dot.active{background:radial-gradient(circle,#fff 0 2.5px,transparent 3px)}

/* welcome */
.welcome-mark{left:55px;top:422px;width:33px;height:33px;border-radius:50%;background:var(--green)}
.welcome-title{left:96px;top:419px;font-family:"Roboto",sans-serif;font-weight:300;font-size:16px;line-height:19px;color:var(--heading)}
.welcome-title .big{font-size:17px}
.welcome-title .accent{color:#2a8fd6}
.welcome-text{left:56px;top:469px;width:304px;font-size:6.2px;line-height:11.3px;color:#555}
.welcome-text p+p{margin-top:5px}
.read-more{left:56px;top:565px;width:66px;height:17px;border:1px solid #8a7a5a;border-radius:2px;font-size:6.5px;text-align:center;line-height:15px;color:#444}
.video{left:378px;top:422px;width:235px;height:160px;padding:2px;background:linear-gradient(135deg,#2a8fd6,#7cc04a)}
.video-fill{width:100%;height:100%;background:linear-gradient(180deg,#f2f2f2,#d9d9d9);display:flex;align-items:center;justify-content:center}
.play{width:26px;height:19px;background:#e22b2b;border-radius:4px;display:flex;align-items:center;justify-content:center}

/* features */
.features{left:0;top:613px;width:668px;height:281px;background:linear-gradient(135deg,#1458a8,#0d4f9f 60%,#165fb3)}
.monitor{left:114px;top:640px;width:182px;height:218px;background:linear-gradient(180deg,#cfd6dd 0%,#8fa0ae 60%,#dde1e5 100%);border-radius:4px}
.features-title{left:334px;top:653px;font-family:"Roboto",sans-serif;font-weight:400;font-size:22px;color:var(--white)}
.feature-icon{position:absolute;left:339px;width:36px;height:36px;border-radius:50%;border:1.5px solid #fff;display:flex;align-items:center;justify-content:center}
.feature-head{position:absolute;left:388px;font-family:"Roboto",sans-serif;font-weight:400;font-size:9px;color:var(--white)}
.feature-text{position:absolute;left:388px;width:170px;font-size:6px;line-height:11.5px;color:#e6eefa}

/* cards */
.card{position:absolute;top:929px;width:129px}
.card-img{width:129px;height:87px;border:2px solid #fff;box-shadow:0 0 0 1px #ddd}
.card-title{margin-top:14px;font-family:"Roboto",sans-serif;font-weight:400;font-size:7.6px;color:#333;white-space:nowrap}
.card-text{margin-top:6px;font-size:6px;line-height:11.6px;color:#555;height:46px}
.card-link{margin-top:5px;font-family:"Roboto",sans-serif;font-size:6.5px;color:#333;display:flex;align-items:center;gap:3px}

/* footer */
.site-footer{left:0;top:1136px;width:668px;height:64px;background:var(--blue-footer);color:var(--white)}
.foot-head{position:absolute;top:17px;font-family:"Roboto",sans-serif;font-size:11px}
.foot-line{position:absolute;top:33px;font-size:6.5px}
.social{position:absolute;top:22px;width:14px;height:14px;border-radius:50%;background:#fff}
</style>
</head>
<body>

<header class="site-header">
  <div class="abs brand">
    <div class="brand-mark"></div>
    <div>
      <div class="brand-name">TIN LANTERN WALK</div>
      <div class="brand-tag">Lit for Every Exit</div>
    </div>
  </div>
  <div class="abs contact-icon">
    <svg width="9" height="9" viewBox="0 0 24 24"><path fill="#444" d="M6.6 10.8a15 15 0 0 0 6.6 6.6l2.2-2.2c.3-.3.7-.4 1-.2 1.1.4 2.3.6 3.6.6.6 0 1 .4 1 1V20c0 .6-.4 1-1 1A17 17 0 0 1 3 4c0-.6.4-1 1-1h3.5c.6 0 1 .4 1 1 0 1.3.2 2.5.6 3.6.1.3 0 .7-.2 1z"/></svg>
  </div>
  <div class="abs contact-lines">Ph: (02) 8147 2290<br>info@tin-lantern-walk.com</div>
  <div class="abs search"><span>SEARCH</span>
    <svg width="7" height="7" viewBox="0 0 10 10"><circle cx="4" cy="4" r="3" stroke="#222" stroke-width="1.5" fill="none"/><path d="M6.2 6.2 9 9" stroke="#222" stroke-width="1.5"/></svg>
  </div>
</header>

<nav class="abs main-nav">
  <div class="nav-item nav-home">HOME</div>
  <div class="nav-item" style="left:134px">CLAIM</div>
  <div class="nav-sep" style="left:167px"></div>
  <div class="nav-item" style="left:189px">PROCESS</div>
  <div class="nav-sep" style="left:235px"></div>
  <div class="nav-item" style="left:256px">RESPONSIBILITY</div>
  <div class="nav-sep" style="left:327px"></div>
  <div class="nav-item" style="left:347px">COSTS</div>
  <div class="nav-sep" style="left:387px"></div>
  <div class="nav-item" style="left:406px">FINISHING</div>
  <div class="nav-sep" style="left:459px"></div>
  <div class="nav-item" style="left:475px">BLOG</div>
  <div class="nav-sep" style="left:508px"></div>
  <div class="nav-item" style="left:527px">CONTACT US</div>
</nav>

<section>
  <div class="abs hero" role="img" aria-label="Close-up photo of a framed escape and rescue floor plan on a wall"></div>
  <h1 class="abs hero-title">LIT FOR EVERY EXIT</h1>
  <p class="abs hero-text">Duis aute irure dolor in reprehenderit in voluptate velit esse cillum dolore eu fugiat nulla pariatur. Excepteur sint</p>
  <div class="abs hero-btn">REQUEST INFO</div>
  <div class="abs dots"><span class="dot active"></span><span class="dot"></span><span class="dot"></span><span class="dot"></span></div>
</section>

<section>
  <div class="abs welcome-mark"></div>
  <h2 class="abs welcome-title">Welcome to<br><span class="big">TIN <span class="accent">LANTERN</span> WALK</span></h2>
  <div class="abs welcome-text">
    <p>Lorem ipsum dolor sit amet, consectetur adipiscing elit, sed do eiusmod tempor incididunt ut labore et dolore magna aliqua. Ut enim ad minim veniam, quis nostrud exercitation ullamco laboris nisi ut aliquip ex ea commodo consequat. Duis aute irure dolor in reprehenderit in voluptate velit esse cillum dolore eu fugiat nulla pariatur. Excepteur sint occaecat cupidatat non proident.</p>
    <p>Lorem ipsum dolor sit amet, consectetur adipiscing elit, sed do eiusmod tempor incididunt ut labore et dolore magna aliqua. Ut enim ad minim veniam, quis nostrud exercitation ullamco laboris nisi ut aliquip ex ea commodo consequat. Duis aute irure dolor in reprehenderit in voluptate</p>
  </div>
  <div class="abs read-more">READ MORE &#10140;</div>
  <div class="abs video">
    <div class="video-fill" role="img" aria-label="Explainer video still: sketched fire engine and two people thinking about safety signs">
      <div class="play"><svg width="8" height="9" viewBox="0 0 8 9"><path d="M0 0 8 4.5 0 9z" fill="#fff"/></svg></div>
    </div>
  </div>
</section>

<section>
  <div class="abs features"></div>
  <div class="abs monitor" role="img" aria-label="Desktop monitor showing a row of framed evacuation plans"></div>
  <h2 class="abs features-title">Tin Lantern Walk</h2>

  <div class="feature-icon" style="top:700px">
    <svg width="18" height="18" viewBox="0 0 20 20" fill="none" stroke="#fff" stroke-width="2"><path d="M10 3 6 9h8z"/><path d="M4 12l-2 4h7"/><path d="M16 12l2 4h-6"/></svg>
  </div>
  <div class="feature-head" style="top:697px">RESPONSIBILITY</div>
  <p class="feature-text" style="top:713px">Escape and rescue plans are an essential component of industrial fire protection organization. They should</p>

  <div class="feature-icon" style="top:758px">
    <svg width="18" height="18" viewBox="0 0 20 20"><circle cx="10" cy="10" r="8" fill="#fff"/><path d="M10 10V2a8 8 0 0 1 8 8z" fill="#0d4f9f"/><path d="M11 9V3a7 7 0 0 1 6 6z" fill="#fff"/></svg>
  </div>
  <div class="feature-head" style="top:755px">COSTS</div>
  <p class="feature-text" style="top:771px">Your requirements are our basis: We pay attention to your money. We act in your interest. Any form..</p>

  <div class="feature-icon" style="top:815px">
    <svg width="18" height="16" viewBox="0 0 20 18"><rect x="1" y="1" width="18" height="12" rx="1" fill="#fff"/><rect x="3" y="3" width="14" height="8" fill="#0d4f9f"/><rect x="8" y="13" width="4" height="3" fill="#fff"/><rect x="5" y="16" width="10" height="2" fill="#fff"/></svg>
  </div>
  <div class="feature-head" style="top:812px">FINISHING</div>
  <p class="feature-text" style="top:828px">Lorem ipsum dolor sit amet, consectetur adipiscing elit, sed do eiusmod tempor incididunt ut labore</p>
</section>

<section>
  <article class="card" style="left:54px">
    <div class="card-img" role="img" aria-label="Framed escape and rescue plan leaning against a wall" style="background:linear-gradient(135deg,#e8e4da,#c9b98a)"></div>
    <h3 class="card-title">WHAT ARE ESCAPE &amp; RESCUE PLANS?</h3>
    <p class="card-text">It is burning. Now it is: get out of the building. To safety. Escape and rescue plans are an important guide and also an essential tool for training people for the right</p>
    <div class="card-link">CLICK HERE <svg width="7" height="7" viewBox="0 0 10 10"><circle cx="5" cy="5" r="5" fill="#333"/><path d="M4 2.5 6.5 5 4 7.5" stroke="#fff" stroke-width="1.5" fill="none"/></svg></div>
  </article>
  <article class="card" style="left:198px">
    <div class="card-img" role="img" aria-label="Construction site with cranes lit up at dusk" style="background:linear-gradient(180deg,#27406e,#5a5a6a 60%,#c98a3a)"></div>
    <h3 class="card-title">THE DEMANDS ON OUR WORK</h3>
    <p class="card-text">The function of the escape and rescue plan is with us at any time at the center. We are aware that we can contribute with our work makes an important contribution</p>
    <div class="card-link">CLICK HERE <svg width="7" height="7" viewBox="0 0 10 10"><circle cx="5" cy="5" r="5" fill="#333"/><path d="M4 2.5 6.5 5 4 7.5" stroke="#fff" stroke-width="1.5" fill="none"/></svg></div>
  </article>
  <article class="card" style="left:341px">
    <div class="card-img" role="img" aria-label="Team of three reviewing a building plan in an office" style="background:linear-gradient(135deg,#d8d8d4,#6a625a)"></div>
    <h3 class="card-title">OUR QUALITY GUARANTEE</h3>
    <p class="card-text">The function of the escape and rescue plan is with us at any time at the center. We are aware that we can contribute with our work makes an important contribution</p>
    <div class="card-link">CLICK HERE <svg width="7" height="7" viewBox="0 0 10 10"><circle cx="5" cy="5" r="5" fill="#333"/><path d="M4 2.5 6.5 5 4 7.5" stroke="#fff" stroke-width="1.5" fill="none"/></svg></div>
  </article>
  <article class="card" style="left:483px">
    <div class="card-img" role="img" aria-label="Person on the phone at a desk with a binder" style="background:linear-gradient(135deg,#f0f0ee,#a89a90)"></div>
    <h3 class="card-title">SUCCESS FACTOR: EFFICIENCY</h3>
    <p class="card-text">Draw? That's part of it. But only individual programming project - in DraftCore or Ridgeline PlanStudio - provide real perfor-mance! Many of the projects</p>
    <div class="card-link">CLICK HERE <svg width="7" height="7" viewBox="0 0 10 10"><circle cx="5" cy="5" r="5" fill="#333"/><path d="M4 2.5 6.5 5 4 7.5" stroke="#fff" stroke-width="1.5" fill="none"/></svg></div>
  </article>
</section>

<footer class="abs site-footer">
  <div class="foot-head" style="left:55px">COPYRIGHT</div>
  <div class="foot-line" style="left:55px">(c) 2015 tin-lantern-walk.com . All rights reserved.</div>
  <div class="foot-head" style="left:280px">ASK? WE LOOK FORWARD TO YOUR CALL:</div>
  <div class="foot-line" style="left:280px">Phone : +49 (0) 6151/42 17 30 0 , Email : info@tin-lantern-walk.com</div>
  <span class="social" style="left:551px"></span>
  <span class="social" style="left:567px"></span>
  <span class="social" style="left:583px"></span>
  <span class="social" style="left:599px"></span>
</footer>

</body>
</html>
```